Brochure/flyer for our trip to Paris

Our company is taking us all on a summer trip to Paris. We have some key information that we need to tell everybody about the trip. We think a nicely designed brochure or flyer, which uses our brand colours and guidelines, would be something nice to keep during the trip and as a memento afterwards.

We are looking for a brochure or a flyer which contains all the info in the attached document.

This needs to happen really fast as we actually go to Paris on the 13th August. We also need time to print it!

We can provide a library of icons. All images in the document can be changed. you don't have to use the images in the document.

Target Market(s)

People in our company. They are fun and as this is for a party the flyer needs to feel uplifting.

Industry/Entity Type

Health

Font styles to use
Other font styles liked:
• Nexa - please see attached font.

Requirements
Must have
• Designers must stick to our brand guideline, font and the colours we use.
• Please also see attached content for the flyer.
• This website shows our style - https://www.kelotrix.com/fr
Should not have
• Please don't make it too tacky or too much about French things. It can be a bit playful but not too much.

```html
<!DOCTYPE html>
<html lang="en">
<head>
<meta charset="utf-8">
<title>A Summer Trip to Paris – Kelotrix</title>
<link rel="stylesheet" href="https://fonts.googleapis.com/css2?family=Roboto+Condensed:wght@400;700&family=Lato:wght@400;700&display=swap">
<style>
  :root {
    --brand-blue: #2f8ae6;
    --brand-blue-deep: #1a6fd6;
    --brand-blue-light: #4aa6f5;
    --brand-teal: #5ed6d2;
    --ink: #222a33;
    --navy: #1d4f8f;
    --paper: #ffffff;
    --paper-shade: #ecedf0;
    --backdrop: #e6e8eb;
  }
  * { box-sizing: border-box; margin: 0; padding: 0; }
  html, body { width: 1200px; height: 900px; overflow: hidden; }
  body { background: var(--backdrop); font-family: "Lato", sans-serif; color: var(--ink); }

  .spread { position: absolute; left: 63px; top: 65px; width: 1075px; height: 765px; display: flex; box-shadow: 0 6px 24px rgba(0,0,0,.18); }
  .page { position: relative; width: 537.5px; height: 765px; overflow: hidden; background: var(--paper); }
  .page-art { position: absolute; inset: 0; width: 100%; height: 100%; }

  /* left page */
  .headline { position: absolute; left: 32px; top: 32px; font-family: "Roboto Condensed", sans-serif; font-weight: 700; font-size: 46px; color: var(--paper); letter-spacing: .5px; }
  .date-badge { position: absolute; left: 266px; top: 110px; width: 152px; height: 152px; border-radius: 50%; background: var(--paper); display: flex; align-items: center; justify-content: center; }
  .date-badge-inner { width: 134px; height: 134px; border-radius: 50%; background: var(--brand-teal); display: flex; flex-direction: column; align-items: center; justify-content: center; font-family: "Roboto Condensed", sans-serif; font-weight: 700; color: var(--navy); line-height: 1; }
  .date-badge-inner .on { font-size: 30px; }
  .date-badge-inner .month { font-size: 36px; margin-top: 4px; }

  .section-title { position: absolute; left: 30px; font-family: "Roboto Condensed", sans-serif; font-weight: 700; font-size: 19px; color: var(--brand-blue-deep); }
  .travel-title { top: 200px; }
  .hotel-title { top: 434px; }
  .journey-tag { position: absolute; left: 32px; height: 26px; padding: 0 8px 0 6px; background: #a9ece9; font-family: "Roboto Condensed", sans-serif; font-size: 17px; line-height: 26px; color: var(--ink); }
  .outward-tag { top: 250px; width: 218px; }
  .return-tag { top: 334px; width: 218px; }
  .details { position: absolute; left: 40px; list-style: none; font-size: 12px; line-height: 23px; color: var(--ink); }
  .details li { display: flex; align-items: center; gap: 6px; }
  .details li::before { content: "✣"; color: var(--brand-blue); font-size: 10px; }
  .outward-list { top: 278px; }
  .return-list { top: 370px; }
  .hotel-line { position: absolute; left: 34px; top: 470px; display: flex; align-items: center; gap: 8px; font-size: 11.5px; }
  .phone-line { position: absolute; left: 34px; top: 494px; display: flex; align-items: center; gap: 8px; font-family: "Lato", sans-serif; font-weight: 700; font-style: italic; font-size: 19px; color: var(--ink); }

  .brand-name { font-family: "Roboto Condensed", sans-serif; font-weight: 400; }
  .footer-brand { position: absolute; left: 32px; top: 655px; font-size: 58px; color: var(--paper); }
  .footer-contact { position: absolute; left: 222px; top: 662px; width: 282px; text-align: center; color: var(--paper); font-family: "Roboto Condensed", sans-serif; }
  .footer-contact .lead { font-style: italic; font-size: 14px; }
  .footer-contact .call { font-weight: 700; font-size: 28px; letter-spacing: 1px; margin-top: 2px; }
  .footer-contact .web { font-size: 14px; letter-spacing: 4px; margin-top: 2px; }

  /* right page */
  .cover-brand { position: absolute; left: 0; right: 0; top: 628px; text-align: center; font-size: 64px; color: var(--brand-blue-light); line-height: 1; }
  .cover-rule { position: absolute; left: 148px; top: 698px; width: 268px; height: 2px; background: var(--ink); }
  .cover-web { position: absolute; left: 0; right: 0; top: 708px; text-align: center; font-family: "Roboto Condensed", sans-serif; font-weight: 700; font-size: 16px; letter-spacing: 4px; color: var(--ink); }
</style>
</head>
<body>
<main class="spread">

  <section class="page page-left">
    <svg class="page-art" viewBox="0 0 537.5 765" preserveAspectRatio="none" aria-hidden="true">
      <defs>
        <linearGradient id="bandBlue" x1="0" y1="0" x2="1" y2="0">
          <stop offset="0" stop-color="#2a7fe0"/>
          <stop offset="1" stop-color="#4aa6f5"/>
        </linearGradient>
        <linearGradient id="paperFade" x1="0" y1="0" x2="1" y2="0">
          <stop offset="0" stop-color="#ffffff"/>
          <stop offset="1" stop-color="#e8e9ec"/>
        </linearGradient>
      </defs>
      <rect width="537.5" height="765" fill="url(#paperFade)"/>
      <polygon points="0,0 537.5,0 537.5,262 0,92" fill="url(#bandBlue)"/>
      <polygon points="0,92 537.5,262 537.5,272 0,104" fill="#5ed6d2"/>
      <polygon points="0,520 537.5,640 537.5,765 0,765" fill="url(#bandBlue)"/>
      <polygon points="0,512 537.5,632 537.5,642 0,522" fill="#5ed6d2"/>
    </svg>

    <h1 class="headline">A SUMMER TRIP TO PARIS</h1>
    <div class="date-badge"><div class="date-badge-inner"><span class="on">on 13th</span><span class="month">August</span></div></div>

    <h2 class="section-title travel-title">Travel Information:</h2>
    <div class="journey-tag outward-tag">Outward Journey 13/08/16:</div>
    <ul class="details outward-list">
      <li>Meet at Kings Cross St Pancras International Station no later than 6:55am.</li>
      <li>Our train departs at 7:55am and arrives in paris at 11:17am local time.</li>
    </ul>
    <div class="journey-tag return-tag">Return Journey 14/08/16:</div>
    <ul class="details return-list">
      <li>Meet at Gare Du Nord no later than 2pm .</li>
      <li>Our train departs at 3:13pm and arrives in London at 4:30pm local time.</li>
    </ul>

    <h2 class="section-title hotel-title">Hotel Information:</h2>
    <p class="hotel-line">
      <svg width="18" height="16" viewBox="0 0 18 16" aria-hidden="true"><path d="M9 1 1 8h2.5v7h4v-4.5h3V15h4V8H17z" fill="#2f8ae6"/></svg>
      HOTEL DES LYS DORÉS 8, rue des Tanneurs 75001 Paris France
    </p>
    <p class="phone-line">
      <svg width="17" height="17" viewBox="0 0 24 24" aria-hidden="true"><path d="M6.6 10.8a15.1 15.1 0 0 0 6.6 6.6l2.2-2.2c.3-.3.7-.4 1-.2 1.1.4 2.3.6 3.6.6.6 0 1 .4 1 1V20c0 .6-.4 1-1 1A17 17 0 0 1 3 4c0-.6.4-1 1-1h3.5c.6 0 1 .4 1 1 0 1.3.2 2.5.6 3.6.1.3 0 .7-.2 1z" fill="#2f8ae6"/></svg>
      +33 1 40 55 18 07
    </p>

    <div class="brand-name footer-brand">Kelotrix</div>
    <div class="footer-contact">
      <p class="lead">For more information visit our website or call us</p>
      <p class="call">CALL US: 04 5550 0192</p>
      <p class="web">www.kelotrix.com</p>
    </div>
  </section>

  <section class="page page-right">
    <svg class="page-art" viewBox="0 0 537.5 765" preserveAspectRatio="none">
      <defs>
        <linearGradient id="skyTower" x1="0" y1="0" x2="0" y2="1">
          <stop offset="0" stop-color="#c9d3d8"/>
          <stop offset="1" stop-color="#5f6e76"/>
        </linearGradient>
        <linearGradient id="streetSquare" x1="0" y1="0" x2="0" y2="1">
          <stop offset="0" stop-color="#d9dde0"/>
          <stop offset="1" stop-color="#7d7a72"/>
        </linearGradient>
        <linearGradient id="riverNight" x1="0" y1="0" x2="0" y2="1">
          <stop offset="0" stop-color="#4a6a9a"/>
          <stop offset="0.55" stop-color="#2b3550"/>
          <stop offset="1" stop-color="#9a6a3a"/>
        </linearGradient>
        <radialGradient id="nightVenue" cx=".5" cy=".5" r=".6">
          <stop offset="0" stop-color="#b8312a"/>
          <stop offset="1" stop-color="#1a1c38"/>
        </radialGradient>
      </defs>
      <rect width="537.5" height="765" fill="#ffffff"/>
      <polygon role="img" aria-label="Photo of the Eiffel Tower and a bridge over the Seine under a cloudy sky" points="0,0 537.5,0 537.5,270 300,345 240,345 0,270" fill="url(#skyTower)"/>
      <polygon role="img" aria-label="Photo of a column monument on a city square with visitors" points="0,318 200,375 200,620 0,640" fill="url(#streetSquare)"/>
      <polygon role="img" aria-label="Photo of a riverside skyline lit up at dusk" points="340,375 537.5,318 537.5,640 340,620" fill="url(#riverNight)"/>
      <line x1="0" y1="312" x2="537.5" y2="655" stroke="#ffffff" stroke-width="10"/>
      <line x1="537.5" y1="312" x2="0" y2="655" stroke="#ffffff" stroke-width="10"/>
      <polygon points="120,312 230,345 220,360 100,325" fill="#2f8ae6"/>
      <polygon points="417,312 307,345 317,360 437,325" fill="#2f8ae6"/>
      <polygon points="60,640 230,585 240,600 80,655" fill="#2f8ae6"/>
      <polygon points="477,640 307,585 297,600 457,655" fill="#2f8ae6"/>
      <polygon points="0,640 200,620 340,620 537.5,640 537.5,660 0,660" fill="#ffffff"/>
      <polygon points="0,648 220,600 225,606 0,656" fill="#5ed6d2"/>
      <polygon points="537.5,648 317,600 312,606 537.5,656" fill="#5ed6d2"/>
      <circle cx="268" cy="450" r="128" fill="#ffffff"/>
      <circle cx="268" cy="450" r="120" fill="#2f8ae6"/>
      <circle cx="268" cy="450" r="108" fill="#ffffff"/>
      <circle cx="268" cy="450" r="102" fill="#5ed6d2"/>
      <circle role="img" aria-label="Photo of a famous Paris cabaret front lit in red at night" cx="268" cy="450" r="92" fill="url(#nightVenue)"/>
    </svg>

    <div class="brand-name cover-brand">Kelotrix</div>
    <div class="cover-rule"></div>
    <div class="cover-web">www.kelotrix.com</div>
  </section>

</main>
</body>
</html>
```